International PR and marketing agency needs website design

We need a branding website, for a company based in the US (Washington DC). We are a communication (PR, marketing, social media) agency. We already have the copy, and we have some example websites (some major agencies), that we like.
For example:
https://tallorquinbeam.example/
https://zurvexglobal.example/
https://pemrat.example/
https://qfn-omnis.example/
https://www.roskavert.example/
The website must be a multi-language site, we will add the new languages step-by-step.
We would like to upload content continuously.
The website has to have sub-pages (segments), and news part.
Target Market(s)
Global
Industry/Entity Type
Public relations, Communications, Marketing, Social Media
Number of Pages Required
5+ page
Font styles to use
Other font styles liked:
- Well readable, modern style.
Look and feel
Each slider illustrates characteristics of the customer's brand and the style your logo design should communicate.

```html
<!DOCTYPE html>
<html lang="en">
<head>
<meta charset="utf-8">
<title>Kestrova – Communications Agency</title>
<link rel="stylesheet" href="https://fonts.googleapis.com/css2?family=Nunito:wght@400;600;700;800&family=Poppins:wght@400;500;600&family=Roboto+Condensed:wght@700&display=swap">
<style>
:root{
  --red:#e30a1e;
  --crimson:#c0103a;
  --plum:#8e1462;
  --wine:#a01351;
  --ink:#222;
  --muted:#666;
  --blush:#fbe9ef;
  --footer:#161616;
  --white:#fff;
}
*{box-sizing:border-box;margin:0;padding:0}
html,body{width:1200px;height:3917px;overflow:hidden}
body{position:relative;font-family:"Poppins",sans-serif;color:var(--ink);background:var(--white)}
.abs{position:absolute}
h1,h2,h3{font-family:"Nunito",sans-serif;font-weight:700;line-height:1.15}
.btn{position:absolute;display:flex;align-items:center;justify-content:center;border-radius:20px;
  background:linear-gradient(90deg,var(--red),var(--plum));color:#fff;font:600 13px "Poppins",sans-serif;text-transform:uppercase;text-decoration:none}

/* hero */
.hero{position:absolute;left:0;top:0;width:1200px;height:686px;overflow:hidden;
  background:linear-gradient(180deg,#fdeef3 0%,#fbe4ec 100%)}
.hero-corner{position:absolute;left:-7px;top:-152px;width:304px;height:304px;border-radius:50%;background:#fff}
.hero-blob{position:absolute;left:502px;top:129px;width:700px;height:700px;border-radius:50%;
  background:linear-gradient(160deg,var(--red) 10%,var(--crimson) 55%,var(--plum) 100%)}
.hero-photo{position:absolute;left:527px;top:143px;width:542px;height:542px;border-radius:50%;
  border:10px solid #fff;background:linear-gradient(140deg,#5a5a5a,#a88f7c 45%,#3d3a3d)}
.brand{position:absolute;left:111px;top:14px;font:800 30px "Nunito",sans-serif;color:var(--red);display:flex;align-items:center;gap:8px}
.brand i{width:14px;height:14px;border-radius:50%;background:var(--red);display:block}
.nav{position:absolute;left:361px;top:30px;display:flex;gap:28px;font:500 14px "Poppins",sans-serif}
.nav a{color:#222;text-decoration:none}
.nav a.active{color:var(--red)}
.lang{position:absolute;left:1015px;top:28px;display:flex;align-items:center;gap:8px;font:500 14px "Poppins",sans-serif}
.lang .flag{width:24px;height:24px;border-radius:50%;background:#c8283c}
.hero-title{position:absolute;left:111px;top:252px;font:600 54px/1 "Nunito",sans-serif;color:var(--wine)}
.hero-text{position:absolute;left:111px;top:317px;width:370px;font-size:14px;line-height:21px;color:#333}
.slide-btn{position:absolute;top:584px;width:32px;height:32px;border-radius:50%;display:flex;align-items:center;justify-content:center}

/* who */
.who-mark{position:absolute;left:100px;top:771px;width:444px;height:444px;border-radius:50%;
  background:linear-gradient(150deg,#c51937,#8c1453 60%,#6a1250)}
.who-dot{position:absolute;left:539px;top:808px;width:66px;height:66px;border-radius:50%;background:var(--red)}
.who-title{position:absolute;left:633px;top:780px;font-size:40px;font-weight:600;color:#2a2a2a}
.copy{position:absolute;font-size:13.5px;line-height:26px;color:#555;text-align:justify}

/* expertise */
.expertise{position:absolute;left:0;top:1311px;width:1200px;height:691px;
  background:linear-gradient(180deg,var(--red) 0%,var(--crimson) 55%,var(--plum) 100%)}
.exp-title{position:absolute;left:0;width:1200px;top:92px;text-align:center;font-size:40px;font-weight:600;color:#fff}
.tab{position:absolute;top:164px;width:167px;height:40px;border-radius:20px;border:1.5px solid rgba(255,255,255,.85);
  display:flex;align-items:center;justify-content:center;color:#fff;font:600 16px "Nunito",sans-serif}
.tab.on{background:#fff;color:var(--red)}
.tab.on:after{content:"";position:absolute;bottom:-10px;left:76px;border:8px solid transparent;border-top-color:#fff;border-bottom:0}
.card{position:absolute;top:248px;width:304px;height:338px;display:flex;align-items:flex-end;justify-content:center;
  padding-bottom:26px;color:#fff;font:700 16px "Nunito",sans-serif;text-align:center;line-height:26px}
.card.a{background:linear-gradient(180deg,#4a5764,#2f3138 60%,#1d1d22)}
.card.b{background:linear-gradient(180deg,#cfc7b7,#a7957b 55%,#5a4a38)}
.card.c{background:linear-gradient(180deg,#d5d4d0,#8d8f95 55%,#3b3c44)}
.round{position:absolute;width:34px;height:34px;border-radius:50%;background:#fff;display:flex;align-items:center;justify-content:center}

/* news */
.news-title{position:absolute;left:0;width:1200px;top:2090px;text-align:center;font-size:40px;font-weight:600;color:var(--wine)}
.news-card{position:absolute;width:466px;height:240px;border:3px solid #e6e6e6;background:#fff}
.news-img{position:absolute;width:186px;height:245px}
.news-body{position:absolute;width:225px}
.news-body h3{font-size:21px;font-weight:600;color:#222}
.news-body .date{margin-top:14px;font-size:13.5px;color:var(--red);display:flex;gap:6px;align-items:center}
.news-body p{margin-top:12px;font-size:12.5px;line-height:21px;color:#666}
.news-body a{display:block;margin-top:12px;font-size:13px;color:var(--red);text-decoration:underline}

/* work */
.work{position:absolute;left:0;top:2887px;width:1200px;height:623px;overflow:hidden;
  background:linear-gradient(180deg,var(--red) 0%,var(--crimson) 50%,var(--plum) 100%)}
.work-title{position:absolute;left:111px;top:88px;font-size:40px;font-weight:600;color:#fff}
.work .copy{color:#fff}
.work-img{position:absolute;left:619px;top:102px;width:470px;height:418px;
  background:linear-gradient(135deg,#1d2f3c,#3a6c82 45%,#0f1a22)}
.btn.light{background:#fff;color:var(--red)}

/* footer */
.footer{position:absolute;left:0;top:3510px;width:1200px;height:407px;background:var(--footer);color:#fff;overflow:hidden}
.f-icon{position:absolute;left:135px;width:52px;height:52px;border-radius:50%;border:2px solid #fff;display:flex;align-items:center;justify-content:center}
.f-text{position:absolute;left:201px;font-size:12.5px;line-height:21px}
.f-head{position:absolute;font:700 20px "Roboto Condensed",sans-serif}
.links{position:absolute;left:465px;top:141px;list-style:none;font-size:13px;line-height:24px}
.links li:before{content:"»";margin-right:18px}
.field{position:absolute;border:1px solid #bbb;font-size:11px;padding:9px 15px;color:#eee}
.submit{position:absolute;left:887px;top:238px;width:205px;height:35px;background:var(--red);display:flex;align-items:center;justify-content:center;font:600 12px "Poppins",sans-serif}
.copyright{position:absolute;left:0;width:1200px;top:333px;text-align:center;font-size:13px}
</style>
</head>
<body>

<section class="hero">
  <div class="hero-corner"></div>
  <div class="hero-blob"></div>
  <div class="hero-photo" role="img" aria-label="Photo of a team of young colleagues gathered around a laptop"></div>
  <div class="brand"><i></i>Kestrova</div>
  <nav class="nav">
    <a class="active" href="#">Home</a><a href="#">Who we Are</a><a href="#">Our Expertise</a><a href="#">News</a><a href="#">Our Work</a><a href="#">KestrovaLink</a><a href="#">Contact</a>
  </nav>
  <div class="lang"><span class="flag"></span>Eng ▾</div>
  <h1 class="hero-title">Kestrova</h1>
  <p class="hero-text">Lorem ipsum dolor sit amet, consectetur adipiscing elit, sed do eiusmod tempor incididunt ut labore et dolore magna aliqua.</p>
  <a class="btn" style="left:113px;top:393px;width:135px;height:36px">Get Started</a>
  <div class="slide-btn" style="left:113px;background:#222"><svg width="10" height="10" viewBox="0 0 10 10"><path d="M6.5 1.5 3 5l3.5 3.5" stroke="#fff" stroke-width="1.6" fill="none"/></svg></div>
  <div class="slide-btn" style="left:164px;background:var(--red)"><svg width="10" height="10" viewBox="0 0 10 10"><path d="M3.5 1.5 7 5 3.5 8.5" stroke="#fff" stroke-width="1.6" fill="none"/></svg></div>
</section>

<section class="who">
  <div class="who-mark" role="img" aria-label="Circular brand graphic filled with a red-toned photo of people at work"></div>
  <div class="who-dot"></div>
  <h2 class="who-title">Who We Are</h2>
  <p class="copy" style="left:633px;top:842px;width:456px">Our work goes way beyond media relations and marketing services. Our creators and colleagues prepare such campaigns and designs that not only provide the competitive advantage and attention our clients need, but also create values and interaction that last for more generations. For us, it is extremely important to support transparent business processes, client-focused and ethical behavior though the principles and values laid down in our philosophy – that allows us to create true values.</p>
  <p class="copy" style="left:633px;top:1073px;width:456px">Regardless of the time zone and the continent, to be able to offer the best for You, the talented team of Kestrova Solution believes in cross-cultural relations. In other words, we think positive.</p>
  <a class="btn" style="left:633px;top:1172px;width:136px;height:35px">Learn More</a>
</section>

<section class="expertise">
  <h2 class="exp-title">Our Expertise</h2>
  <div class="tab on" style="left:345px">Practices</div>
  <div class="tab" style="left:517px">Influencers</div>
  <div class="tab" style="left:689px">Other Solutions</div>
  <div class="card a" style="left:111px" role="img" aria-label="Photo of business colleagues in discussion">Consumer Products<br>and Services</div>
  <div class="card b" style="left:449px" role="img" aria-label="Photo of a smiling professional in an office">Content &amp; Publishing<br>Strategy</div>
  <div class="card c" style="left:785px" role="img" aria-label="Photo of a team reviewing work at a laptop">Crisis Management</div>
  <div class="round" style="left:40px;top:420px"><svg width="10" height="10" viewBox="0 0 10 10"><path d="M6.5 1.5 3 5l3.5 3.5" stroke="#222" stroke-width="1.6" fill="none"/></svg></div>
  <div class="round" style="left:1127px;top:420px"><svg width="10" height="10" viewBox="0 0 10 10"><path d="M3.5 1.5 7 5 3.5 8.5" stroke="#222" stroke-width="1.6" fill="none"/></svg></div>
</section>

<h2 class="news-title">Our Latest News</h2>

<article class="news-card" style="left:111px;top:2202px"></article>
<div class="news-img" style="left:129px;top:2178px;background:linear-gradient(160deg,#f1f1ef,#b7bcc4 55%,#4d5560)" role="img" aria-label="Photo of people reviewing charts at a desk"></div>
<div class="news-body" style="left:339px;top:2220px"><h3>Duis aute irure dolor</h3><div class="date">▦ Jan 20,2023</div><p>Lorem ipsum dolor sit amet, cons ectetur adipiscing elit, sed do eius mod tempor incididunt ut labore et dolore magna aliqua.</p><a>LEARN MORE</a></div>

<article class="news-card" style="left:622px;top:2202px"></article>
<div class="news-img" style="left:640px;top:2178px;background:linear-gradient(160deg,#f2efe8,#c7a27c 50%,#6e5036)" role="img" aria-label="Photo of a woman working on a laptop"></div>
<div class="news-body" style="left:850px;top:2220px"><h3>Duis aute irure dolor</h3><div class="date">▦ Jan 20,2023</div><p>Lorem ipsum dolor sit amet, cons ectetur adipiscing elit, sed do eius mod tempor incididunt ut labore et dolore magna aliqua.</p><a>LEARN MORE</a></div>

<article class="news-card" style="left:111px;top:2485px"></article>
<div class="news-img" style="left:129px;top:2461px;background:linear-gradient(160deg,#8ea4ab,#4e6269 55%,#2a2e33)" role="img" aria-label="Photo of two colleagues looking at a screen"></div>
<div class="news-body" style="left:339px;top:2503px"><h3>Duis aute irure dolor</h3><div class="date">▦ Jan 20,2023</div><p>Lorem ipsum dolor sit amet, cons ectetur adipiscing elit, sed do eius mod tempor incididunt ut labore et dolore magna aliqua.</p><a>LEARN MORE</a></div>

<article class="news-card" style="left:622px;top:2485px"></article>
<div class="news-img" style="left:640px;top:2461px;background:linear-gradient(160deg,#dcdcd6,#8e8f88 55%,#3c3b38)" role="img" aria-label="Photo of a team meeting around a table"></div>
<div class="news-body" style="left:850px;top:2503px"><h3>Duis aute irure dolor</h3><div class="date">▦ Jan 20,2023</div><p>Lorem ipsum dolor sit amet, cons ectetur adipiscing elit, sed do eius mod tempor incididunt ut labore et dolore magna aliqua.</p><a>LEARN MORE</a></div>

<a class="btn" style="left:532px;top:2747px;width:135px;height:35px">View More</a>

<section class="work">
  <h2 class="work-title">Our Work</h2>
  <p class="copy" style="left:111px;top:155px;width:455px">Our work goes way beyond media relations and marketing services. Our creators and colleagues prepare such campaigns and designs that not only provide the competitive advantage and attention our clients need, but also create values and interaction that last for more generations. For us, it is extremely important to support transparent business processes, client-focused and ethical behavior though the principles and values laid down in our philosophy – that allows us to create true values.</p>
  <p class="copy" style="left:111px;top:386px;width:455px">Regardless of the time zone and the continent, to be able to offer the best for You, the talented team of Kestrova Solution believes in cross-cultural relations. In other words, we think positive.</p>
  <a class="btn light" style="left:111px;top:482px;width:135px;height:35px">Learn More</a>
  <svg class="abs" style="left:0;top:0" width="1200" height="623" fill="none" stroke="#fff" stroke-width="10">
    <path d="M607 168 V87 H774"/>
    <path d="M1089 320 Q1170 325 1210 360"/>
    <path d="M790 623 Q790 560 812 520"/>
  </svg>
  <div class="work-img" role="img" aria-label="Photo of hands on a laptop with floating data dashboards"></div>
</section>

<footer class="footer">
  <div class="f-icon" style="top:96px"><svg width="20" height="22" viewBox="0 0 20 22"><path d="M10 1a7 7 0 0 0-7 7c0 5 7 13 7 13s7-8 7-13a7 7 0 0 0-7-7z" fill="#fff"/><circle cx="10" cy="8" r="2.5" fill="#161616"/></svg></div>
  <p class="f-text" style="top:101px">123, Lorem ipsum dolor sit amet,<br>consectetur adipisc</p>
  <div class="f-icon" style="top:164px"><svg width="20" height="20" viewBox="0 0 20 20"><path d="M4 2l4 1 1 4-2 2c1 2 3 4 5 5l2-2 4 1 1 4-2 1C9 18 2 11 2 4z" fill="#fff"/></svg></div>
  <p class="f-text" style="top:169px">Phone :<br>+1 888 888 8888</p>
  <div class="f-icon" style="top:234px"><svg width="22" height="16" viewBox="0 0 22 16"><rect x="1" y="1" width="20" height="14" rx="2" fill="#fff"/><path d="M1 2l10 7 10-7" stroke="#161616" stroke-width="1.8" fill="none"/></svg></div>
  <p class="f-text" style="top:240px">Email :<br>info@companyname.com</p>

  <h3 class="f-head" style="left:465px;top:100px">QUICK LINKS</h3>
  <ul class="links"><li>Home</li><li>About</li><li>Practice Areas</li><li>Blog</li><li>Faq</li><li>Contact</li></ul>

  <h3 class="f-head" style="left:669px;top:100px">CONTACT US</h3>
  <div class="field" style="left:671px;top:142px;width:205px;height:35px">Name</div>
  <div class="field" style="left:671px;top:190px;width:205px;height:35px">Email</div>
  <div class="field" style="left:671px;top:238px;width:205px;height:35px">Phone</div>
  <div class="field" style="left:887px;top:142px;width:205px;height:83px">Message</div>
  <div class="submit">SUBMIT</div>

  <p class="copyright">© Copyrights 2023 | All Rights Reserved</p>
</footer>

</body>
</html>
```